Recreating a Opt-in for a FREE BOOK for brides.

I need to have an opt-in box recreated to make brides want to get my free book. The opt-in message is already on the mock website. It needs to look graphically pleasing in the colors being used, but bold enough to grab the viewers attention. I am including the link to the website where the graphic needs to be re-created. You'll notice there are two areas where the graphics need to go.

Target Market(s)

Brides

Requirements
Must have
• Begin by looking at the website..http://plorvex.com/tu-gami/
On the homepage is the current "A Gift For You" graphic. (I have included an image of the home page for the circled area that needs to be recreated.) As of now, the graphics looks amateurish. It needs your professional upgrade. The image of the book has also been uploaded as a file for you to use.

In addition, on the FAQ page, there is a graphic that has been created to fit that area of the page to get the book (circled area of the graphic has been uploaded). I need to have the same graphic you are creating for the home page, but adjust it to be placed on this page. When you recreate the graphic for the FAQ page, there are 2 changes to the text:

1. Change the word "Receive" to "Download." (The rest of the sentence should stay the same.)
2. Delete the entire sentence "Or, pay $17.95 at zentrabo or corliss and pembe by clicking here.
Nice to have
• Normal file formats such as jpeg, photoshop or ai are fine.

```html
<!DOCTYPE html>
<html lang="en">
<head>
<meta charset="utf-8">
<title>A Gift For You – Free Bride's Guide Opt-in</title>
<link rel="stylesheet" href="https://fonts.googleapis.com/css2?family=Kalam:wght@400;700&family=Montserrat:wght@700&display=swap">
<style>
  :root {
    --mint: #45e3a1;
    --berry: #a3153a;
    --paper: #ffffff;
    --frame: #222222;
    --cover-light: #f2f4f1;
    --cover-mid: #dfe8e2;
    --cover-accent: #b9e6d2;
  }
  * { margin: 0; padding: 0; box-sizing: border-box; }
  html, body { width: 1200px; height: 1200px; overflow: hidden; background: var(--paper); }
  .canvas {
    position: relative;
    width: 1200px;
    height: 1200px;
    background: var(--paper);
    border: 1px solid var(--frame);
    overflow: hidden;
  }
  .gift-title {
    position: absolute;
    font-family: "Kalam", cursive;
    font-weight: 700;
    font-size: 82px;
    line-height: 1;
    color: var(--mint);
    white-space: nowrap;
    width: 629px;
    text-align: center;
    border-bottom: 3px solid var(--mint);
    padding-bottom: 2px;
  }
  .offer-text {
    position: absolute;
    width: 360px;
    font-family: "Kalam", cursive;
    font-weight: 700;
    font-size: 34px;
    line-height: 52px;
    color: var(--berry);
    text-align: center;
  }
  .book-cover {
    position: absolute;
    border-radius: 3px 5px 5px 3px;
    background: linear-gradient(160deg, var(--cover-light) 0%, var(--cover-mid) 55%, var(--cover-accent) 100%);
    box-shadow: 28px 26px 30px -18px rgba(0,0,0,0.22), inset 8px 0 0 #e8ece9;
  }
  .cta-button {
    position: absolute;
    left: 45px;
    top: 364px;
    width: 336px;
    height: 70px;
    border-radius: 35px;
    background: var(--mint);
    color: #ffffff;
    font-family: "Kalam", cursive;
    font-weight: 700;
    font-size: 40px;
    line-height: 70px;
    text-align: center;
    letter-spacing: 1px;
  }
  .download-note {
    position: absolute;
    left: 646px;
    top: 990px;
    width: 400px;
    font-family: "Montserrat", sans-serif;
    font-weight: 700;
    font-size: 30px;
    line-height: 37px;
    color: var(--mint);
    text-align: center;
  }
  .home-block .gift-title { left: 65px; top: 30px; }
  .home-block .offer-text { left: 25px; top: 146px; }
  .home-block .book-cover { left: 404px; top: 140px; width: 180px; height: 289px; }
  .faq-block .gift-title { left: 477px; top: 558px; }
  .faq-block .offer-text { left: 435px; top: 710px; }
  .faq-block .book-cover { left: 815px; top: 668px; width: 181px; height: 286px; }
</style>
</head>
<body>
<main class="canvas">
  <section class="optin home-block">
    <h2 class="gift-title">A Gift For You !</h2>
    <p class="offer-text">The ultimate<br>Brides Guide For<br>Buying a wedding<br>Cake</p>
    <div class="book-cover" role="img" aria-label="Book cover of The Ultimate Bride's Guide for Buying a Wedding Cake, with a kissing couple and a white tiered cake"></div>
    <a class="cta-button" href="http://plorvex.com/tu-gami/">GET IT NOW</a>
  </section>
  <section class="optin faq-block">
    <h2 class="gift-title">A Gift For You !</h2>
    <p class="offer-text">The ultimate<br>Brides Guide For<br>Buying a wedding<br>Cake</p>
    <div class="book-cover" role="img" aria-label="Book cover of The Ultimate Bride's Guide for Buying a Wedding Cake, with a kissing couple and a white tiered cake"></div>
    <p class="download-note">Download Your Free<br>Copy Now</p>
  </section>
</main>
</body>
</html>
```